We need visit card and a letter paper for our website. thx

We have a beauty clinic in Switzerland.
https://wolkenbachtal.ch
We need a visit card.

Requirements
Must have
• see colors on website

```html
<!DOCTYPE html>
<html lang="en">
<head>
<meta charset="utf-8">
<title>Wolkenbachtal – Business Card</title>
<link href="https://fonts.googleapis.com/css2?family=Exo+2:wght@400;500;700&display=swap" rel="stylesheet">
<style>
  :root {
    --stage: #1e1e20;
    --card: #0a0a0b;
    --accent: #d9508a;
    --ink: #ffffff;
  }
  * { box-sizing: border-box; margin: 0; padding: 0; }
  html, body { width: 1200px; height: 900px; overflow: hidden; }
  body {
    background: var(--stage);
    font-family: "Exo 2", sans-serif;
    color: var(--ink);
    position: relative;
  }
  .card {
    position: absolute;
    left: 230px;
    width: 740px;
    height: 400px;
    background: var(--card);
    border-left: 5px solid var(--accent);
    border-bottom: 5px solid var(--accent);
    box-shadow: 0 14px 30px rgba(0,0,0,0.55);
  }
  .card--front { top: 40px; }
  .card--back { top: 465px; }

  .brand {
    position: absolute;
    display: flex;
    align-items: center;
    gap: 14px;
    font-weight: 500;
    color: var(--ink);
    white-space: nowrap;
  }
  .brand__mark {
    width: 18px; height: 18px;
    border: 2px solid var(--ink);
  }
  .card--front .brand {
    left: 50%; top: 50%;
    transform: translate(-50%, -50%);
    font-size: 54px;
  }
  .card--back .brand {
    left: 50px; top: 150px;
    font-size: 40px;
  }
  .card--back .brand__mark { width: 14px; height: 14px; }

  .divider {
    position: absolute;
    left: 395px; top: 95px;
    width: 2px; height: 230px;
    background: var(--accent);
  }
  .details {
    position: absolute;
    left: 420px; top: 100px;
  }
  .details__name {
    font-size: 28px;
    font-weight: 700;
    font-variant: small-caps;
    letter-spacing: 1px;
  }
  .details__role {
    font-size: 18px;
    color: var(--accent);
    margin-bottom: 18px;
  }
  .contact {
    list-style: none;
    font-size: 20px;
  }
  .contact li {
    display: flex;
    align-items: center;
    gap: 10px;
    line-height: 30px;
  }
  .contact svg { width: 20px; height: 20px; flex: none; }
  .details__address {
    margin-top: 18px;
    font-size: 21px;
    line-height: 28px;
    color: var(--accent);
  }
</style>
</head>
<body>
  <section class="card card--front">
    <div class="brand"><span class="brand__mark"></span>Wolkenbachtal</div>
  </section>

  <section class="card card--back">
    <div class="brand"><span class="brand__mark"></span>Wolkenbachtal</div>
    <div class="divider"></div>
    <div class="details">
      <h1 class="details__name">Dr. Lena Marbach</h1>
      <p class="details__role">FÄ for plastic surgery</p>
      <ul class="contact">
        <li>
          <svg viewBox="0 0 24 24" fill="none" stroke="#d9508a" stroke-width="1.8" stroke-linecap="round" stroke-linejoin="round"><circle cx="12" cy="12" r="10"/><path d="M9 7.5c-.8 0-1.5.7-1.3 1.6.6 3 3.2 5.6 6.2 6.2.9.2 1.6-.5 1.6-1.3l-1.8-1-1 .9c-1.2-.5-2.1-1.4-2.6-2.6l.9-1z"/></svg>
          +41 (0) 800 22 40 60
        </li>
        <li>
          <svg viewBox="0 0 24 24" fill="none" stroke="#d9508a" stroke-width="1.8" stroke-linejoin="round"><rect x="2.5" y="5" width="19" height="14"/><path d="M2.5 5l9.5 8 9.5-8"/></svg>
          hallo@wolkenbachtal.ch
        </li>
        <li>
          <svg viewBox="0 0 24 24" fill="none" stroke="#d9508a" stroke-width="1.8"><circle cx="12" cy="12" r="9.5"/><ellipse cx="12" cy="12" rx="4" ry="9.5"/><path d="M2.5 12h19M4 7h16M4 17h16"/></svg>
          www.wolkenbachtal.ch
        </li>
      </ul>
      <p class="details__address">Lindenweg 24, 7512 Wolkenbach<br>Switzerland</p>
    </div>
  </section>
</body>
</html>
```